Bâtisseur Serein

I need à Web design call KtvSommets

With the following

Home page ( ACCUEIL )
PRODUCT ( JEUX EDUCATIFS )
About page ( QUI SUIS-JE )
Video page ( VIDEO )
Programme ( NOS FORMATIONS )
Books ( LIVRES )
Blog page ( PUBLIEZ ICI )
contact

f ...acebook
t..witter

The language need to be in french i send picture of me as a speaker
Updates

I will add 3 more days for design completetion Added Monday, September 19, 2016

Target Market(s)

business owner and real estate investor

Industry/Entity Type

Call

Coding

Coded - Design and coding required

Number of Pages Required

5+ page

Font styles to use
Sans Serif
Script

Colors
a54499
aaaaaa
7f7f7f

Requirements
Must have
• my project should be same as the power point file and Word Press plug in
Nice to have
• any idea that you feel can improve conversion

```html
<!DOCTYPE html>
<html lang="fr">
<head>
<meta charset="utf-8">
<title>KtvSommets Finances</title>
<link rel="stylesheet" href="https://fonts.googleapis.com/css2?family=Montserrat:wght@300;400;500;600;700&family=Open+Sans:wght@400;600&display=swap">
<style>
:root{
  --purple:#a54499;
  --purple-dark:#8e3684;
  --purple-deep:#5e1b57;
  --grey-header:#7a7a7a;
  --grey-tab:#5c5c5c;
  --grey-footer:#7b7b7b;
  --grey-text:#7f7f7f;
  --grey-line:#aaaaaa;
  --ink:#2b2b2b;
  --white:#ffffff;
}
*{margin:0;padding:0;box-sizing:border-box}
html,body{width:1200px;height:2305px;overflow:hidden;background:var(--white)}
body{position:relative;font-family:"Open Sans",Arial,sans-serif;color:var(--ink)}
.abs{position:absolute}

/* header */
.site-header{left:0;top:0;width:1200px;height:95px;background:var(--grey-header)}
.lang-tab{left:879px;top:0;width:166px;height:28px;background:var(--grey-tab);color:#ddd;font:400 12px/28px "Montserrat",sans-serif;text-align:center;letter-spacing:.5px}
.lang-tab b{color:var(--white);font-weight:600;margin-left:8px}
.brand{left:149px;top:34px;color:var(--white);font:500 26px/1 "Montserrat",sans-serif;letter-spacing:.3px}
.main-nav{top:50px;color:var(--white);font:500 14px/1 "Montserrat",sans-serif;white-space:nowrap}
.nav-active{left:476px;top:90px;width:57px;height:5px;background:var(--purple)}

/* hero */
.hero{left:0;top:95px;width:1200px;height:457px;background:linear-gradient(100deg,#3f6a2a 0%,#5e8a3a 30%,#6f6a4f 55%,#5a3a30 75%,#8a3a3a 100%)}
.hero-title{left:149px;color:var(--white);font-family:"Montserrat",sans-serif;font-weight:700;text-transform:uppercase;letter-spacing:.5px;white-space:nowrap}
.hero-title.small{top:334px;font-size:32px}
.hero-title.large{top:370px;font-size:41px}
.dot{top:517px;width:17px;height:17px;border-radius:50%;background:var(--white)}
.dot.hollow{background:transparent;border:2px solid var(--white)}

/* signup band */
.signup-band{left:0;top:552px;width:1200px;height:103px;background:var(--purple)}
.signup-label{left:180px;top:576px;color:var(--white);font:600 18px/29px "Montserrat",sans-serif}
.signup-input{left:484px;top:588px;width:400px;height:39px;background:var(--white);color:#999;font-size:13px;line-height:39px;padding-left:15px}
.signup-btn{left:891px;top:588px;width:108px;height:39px;background:#111;color:var(--white);font:600 14px/39px "Montserrat",sans-serif;text-align:center}

/* about */
.about-photo{left:149px;top:730px;width:263px;height:258px;background:linear-gradient(135deg,#3a2a26,#7a4a3a 50%,#c2306f)}
.about-frame{left:161px;top:740px;width:243px;height:239px;border:2px solid var(--white)}
.about-title{left:442px;top:726px;font:400 28px/1.2 "Montserrat",sans-serif;color:#222;letter-spacing:.5px}
.about-text{left:442px;top:777px;width:605px;color:var(--grey-text);font-size:14px;line-height:31px}
.btn-purple{left:441px;top:948px;width:124px;height:39px;border-radius:3px;background:linear-gradient(#b253a6,var(--purple-dark));color:var(--white);font:600 12px/39px "Montserrat",sans-serif;text-align:center}

/* programmes */
.programmes{left:0;top:1085px;width:1200px;height:433px;background:linear-gradient(180deg,#a84a9c,#9a3c8e 60%,#a54499)}
.section-title{width:1200px;left:0;text-align:center;font:400 26px/1 "Montserrat",sans-serif;letter-spacing:.5px}
.prog-img{top:1177px;width:441px;height:181px}
.prog-caption{top:1358px;width:441px;height:105px;background:var(--purple-deep);color:var(--white);padding:24px 30px 0}
.prog-caption h3{font:400 19px/1.2 "Open Sans",sans-serif;margin-bottom:5px}
.prog-caption p{font-size:12.5px;line-height:20px;color:#e6c9e2}

/* blogs */
.blog-card{top:1613px;width:293px;height:340px;border:1px solid #cfcfcf;background:var(--white);text-align:center}
.blog-img{width:291px;height:175px}
.blog-card h3{margin-top:24px;color:var(--purple);font:600 16px/1 "Montserrat",sans-serif;letter-spacing:.3px}
.blog-card p{margin:10px auto 0;width:270px;font-size:11.5px;line-height:19.5px;color:var(--grey-text)}
.btn-outline{position:absolute;left:88px;top:287px;width:115px;height:33px;border:2px solid #888;color:#555;font:500 11px/29px "Montserrat",sans-serif}

/* footer */
.site-footer{left:0;top:2016px;width:1200px;height:289px;background:var(--grey-footer);color:var(--white)}
.foot-head{top:2062px;font:500 15px/1 "Montserrat",sans-serif;color:var(--white)}
.foot-links{font-size:13px;line-height:28.5px;color:var(--white)}
.social{top:2093px;width:34px;height:34px;border-radius:50%;background:var(--white);display:flex;align-items:center;justify-content:center}
.foot-note{left:710px;top:2092px;font-size:13px;color:var(--white)}
.news-input{left:711px;top:2117px;width:199px;height:34px;background:var(--white);color:#aaa;font-size:10px;line-height:34px;padding-left:14px}
.news-btn{left:910px;top:2117px;width:93px;height:34px;background:var(--purple);color:var(--white);font:600 12px/34px "Montserrat",sans-serif;text-align:center}
.foot-rule{left:141px;top:2248px;width:885px;height:1px;background:#9a9a9a}
.copyright{left:0;top:2264px;width:1200px;text-align:center;font-size:11px;color:#cfcfcf}
</style>
</head>
<body>

<header class="abs site-header"></header>
<div class="abs lang-tab">LANGUAGE <b>EN</b> / <b style="margin-left:2px">FR</b></div>
<div class="abs brand">KtvSommets Finances</div>
<nav>
  <span class="abs main-nav" style="left:484px">Home</span>
  <span class="abs main-nav" style="left:555px">About</span>
  <span class="abs main-nav" style="left:627px">Videos</span>
  <span class="abs main-nav" style="left:702px">Programme et produits</span>
  <span class="abs main-nav" style="left:899px">Blog</span>
  <span class="abs main-nav" style="left:958px">Contact us</span>
</nav>
<div class="abs nav-active"></div>

<section class="abs hero" role="img" aria-label="Photo d'un conférencier debout sur une terrasse entourée de plantes tropicales"></section>
<div class="abs hero-title small">Donec dictum lectus</div>
<div class="abs hero-title large">Non odio cras a ante</div>
<div class="abs dot hollow" style="left:559px"></div>
<div class="abs dot" style="left:580px"></div>
<div class="abs dot" style="left:600px"></div>
<div class="abs dot" style="left:621px"></div>

<section class="abs signup-band">
  <svg width="1200" height="103" style="position:absolute;left:0;top:0">
    <polygon points="0,0 260,0 120,103 0,103" fill="#9b3d8f" opacity=".6"/>
    <polygon points="380,0 720,0 560,103 300,103" fill="#b04fa4" opacity=".5"/>
    <polygon points="820,0 1200,0 1200,103 960,103" fill="#983a8c" opacity=".5"/>
  </svg>
</section>
<div class="abs signup-label">SIGN UP FOR<br>PROGRAMME ET PRODUITS</div>
<div class="abs signup-input">Email address</div>
<div class="abs signup-btn">SIGN UP</div>

<section>
  <div class="abs about-photo" role="img" aria-label="Portrait souriant du coach en chemise rose"></div>
  <div class="abs about-frame"></div>
  <h2 class="abs about-title">LITTLE ABOUT ME</h2>
  <p class="abs about-text">Curabitur iaculis tempus eros Curabitur vel mi sit amet magna malesuada ultrices Ut nisi erat fermentum vel congue id euismod in elit Fusce ultricies orci ac feugiat suscipit leo massa sodales velit et scelerisque mi tortor at ipsum cligula augue bibendum accumsan vestibulum ut commodo a mi Morbi ornare gravida elit Integer congue augue et malesuada iaculis ipsum dui aliquet felis at cursus magna</p>
  <div class="abs btn-purple">READ MORE</div>
</section>

<section class="abs programmes"></section>
<h2 class="abs section-title" style="top:1126px;color:#fff">PROGRAMME ET PRODUITS</h2>
<div class="abs prog-img" style="left:149px;background:linear-gradient(120deg,#4a4a4a,#8a8a7a 55%,#d8d8cc)" role="img" aria-label="Formation en salle avec un intervenant devant un écran de projection"></div>
<div class="abs prog-caption" style="left:149px">
  <h3>Praesent elementum elit</h3>
  <p>ultricies sit amet porttitor mattis enim In massa libero interdum nec interdum vel blandit sed nulla In W</p>
</div>
<div class="abs prog-img" style="left:610px;background:linear-gradient(120deg,#d8d4c4,#8a7a60 50%,#c8c0a8)" role="img" aria-label="Groupe de participants assis en cercle lors d'un atelier"></div>
<div class="abs prog-caption" style="left:610px">
  <h3>Cum sociis natoque pen</h3>
  <p>ultricies sit amet porttitor mattis enim In massa libero interdum nec interdum vel blandit sed nulla In W</p>
</div>

<h2 class="abs section-title" style="top:1556px;color:#222">LATEST <span style="color:var(--purple)">BLOGS</span></h2>

<article class="abs blog-card" style="left:148px">
  <div class="blog-img" style="background:linear-gradient(135deg,#2a2420,#7a5a3a 55%,#d8d0c0)" role="img" aria-label="Le coach au volant d'une voiture ancienne"></div>
  <h3>BLOG TITTLE HERE</h3>
  <p>Praesent elementum elit at tellus nec ultricies sit amet porttitor mattis enim In massa libero interdum nec interdum vel blandit</p>
  <span class="btn-outline">LEARN MORE</span>
</article>
<article class="abs blog-card" style="left:453px">
  <div class="blog-img" style="background:linear-gradient(135deg,#3a4a2a,#c8a890 50%,#2a2a3a)" role="img" aria-label="Trois personnes posant ensemble lors d'un événement"></div>
  <h3>BLOG TITTLE HERE</h3>
  <p>Praesent elementum elit at tellus nec ultricies sit amet porttitor mattis enim In massa libero interdum nec interdum vel blandit</p>
  <span class="btn-outline">LEARN MORE</span>
</article>
<article class="abs blog-card" style="left:757px">
  <div class="blog-img" style="background:linear-gradient(180deg,#aac4dc,#c89880 55%,#b8b0a0)" role="img" aria-label="Le coach devant un bâtiment historique"></div>
  <h3>BLOG TITTLE HERE</h3>
  <p>Praesent elementum elit at tellus nec ultricies sit amet porttitor mattis enim In massa libero interdum nec interdum vel blandit</p>
  <span class="btn-outline">LEARN MORE</span>
</article>

<footer class="abs site-footer"></footer>
<h4 class="abs foot-head" style="left:148px">USEFULL LINKS</h4>
<div class="abs foot-links" style="left:148px;top:2088px">Home<br>About Us<br>Services<br>Videos</div>
<div class="abs foot-links" style="left:281px;top:2088px">Programme et produits<br>Blogs<br>Contact Us</div>
<h4 class="abs foot-head" style="left:472px">FOLLOW US</h4>
<div class="abs social" style="left:472px" aria-label="Partager">
  <svg width="16" height="16" viewBox="0 0 16 16"><circle cx="12" cy="3" r="2" fill="#333"/><circle cx="4" cy="8" r="2" fill="#333"/><circle cx="12" cy="13" r="2" fill="#333"/><path d="M12 3 4 8 12 13" stroke="#333" stroke-width="1.4" fill="none"/></svg>
</div>
<div class="abs social" style="left:515px" aria-label="Courriel">
  <svg width="16" height="16" viewBox="0 0 16 16"><rect x="1.5" y="3.5" width="13" height="9" fill="none" stroke="#333" stroke-width="1.4"/><path d="M1.5 3.5 8 9 14.5 3.5" fill="none" stroke="#333" stroke-width="1.4"/></svg>
</div>
<div class="abs social" style="left:558px" aria-label="Site web">
  <svg width="16" height="16" viewBox="0 0 16 16"><circle cx="8" cy="8" r="6.3" fill="none" stroke="#333" stroke-width="1.4"/><ellipse cx="8" cy="8" rx="2.6" ry="6.3" fill="none" stroke="#333" stroke-width="1.2"/><path d="M1.7 8h12.6" stroke="#333" stroke-width="1.2"/></svg>
</div>
<div class="abs social" style="left:602px" aria-label="Message">
  <svg width="16" height="16" viewBox="0 0 16 16"><path d="M2 3h12v8H7l-3 3v-3H2z" fill="none" stroke="#333" stroke-width="1.4" stroke-linejoin="round"/></svg>
</div>
<h4 class="abs foot-head" style="left:710px">SIGN UP FOR NEWSLETTERS</h4>
<div class="abs foot-note">Please sign up here for latest news</div>
<div class="abs news-input">EMAIL ADDRESS</div>
<div class="abs news-btn">SUBSCRIBE</div>
<div class="abs foot-rule"></div>
<div class="abs copyright">© 2016 Company Name &nbsp;All right reserved &nbsp;Term of Use</div>

</body>
</html>
```